Print on top the name of the company: (Or Similar)
Bellhaven Cleaning & Disinfecting
Because your standards aren't standard.

We adhere to ALL FHB guidelines for both residential and commercial cleaning.

Infection Control is our ultimate goal.

Instructions:
Opening a residential and commercial cleaning and disinfecting company in south Florida.

Targeting high-end residential clients, commercial and healthcare facilities, specializing in Ambulatory Care Guidelines. With a concentration and expertise in targeting Covid 19 and other transmissible pathogens.

TWLR trained.
Owned and operated by a licensed BSN Registered Nurse specially ​trained in Infection Control Prevention with over 25 years experience. Over two decades in Ambulatory Surgery Center Administration, Director of Nursing and Infection Control Prevention ad Consulting.

Looking to create a business flier that emphasizes Cleaning & Disinfection
along with the standard expectation for residential and Commercial cleaning services

Target Market(s)

Residential & Commercial

Font styles to use
Decorative

Requirements
Must have
• A checklist for cleaning services

```html
<!DOCTYPE html>
<html lang="en">
<head>
<meta charset="utf-8">
<title>Bellhaven Cleaning &amp; Disinfecting – Flyer</title>
<link href="https://fonts.googleapis.com/css2?family=Passion+One:wght@400;700&family=Poppins:wght@400;500;600;700&display=swap" rel="stylesheet">
<style>
  :root{
    --navy:#123f7a;
    --navy-deep:#0c2c5a;
    --blue:#1d64b4;
    --green:#6db33f;
    --green-deep:#4e9a2a;
    --ink:#2b2f38;
    --page:#eef1f4;
    --paper:#ffffff;
  }
  *{box-sizing:border-box;margin:0;padding:0}
  html,body{width:1200px;height:2624px;overflow:hidden;background:var(--page)}
  body{font-family:"Poppins",Arial,sans-serif;color:var(--ink);position:relative}

  .flyer{position:absolute;left:50px;top:452px;width:1100px;height:1720px;background:var(--paper);overflow:hidden;box-shadow:0 6px 24px rgba(0,0,0,.12)}

  .hero-photo{position:absolute;left:500px;top:0;width:600px;height:460px;background:linear-gradient(160deg,#f7f8fa 0%,#d9dee5 55%,#b9c2cc 100%)}
  .hero-swoosh{position:absolute;left:0;top:250px;width:1100px;height:240px}
  .corner-accent{position:absolute;left:0;top:0;width:300px;height:110px}

  .brand-title{position:absolute;left:48px;top:100px;font-family:"Passion One",Impact,sans-serif;font-weight:700;line-height:.9;text-transform:uppercase}
  .brand-title span{display:block;font-size:108px}
  .brand-title .line-name{color:var(--navy)}
  .brand-title .line-cleaning{color:var(--green-deep)}
  .brand-title .line-disinfect{color:var(--navy)}

  .badge{position:absolute;left:815px;top:420px;width:240px;height:240px}

  .mascot{position:absolute;left:40px;top:440px;width:170px;height:170px;border-radius:12px;background:linear-gradient(180deg,#e0443b 0%,#2c5ea8 60%,#f1c27d 100%);opacity:.85}

  .owner-note{position:absolute;left:230px;top:510px;width:560px;font-size:21px;line-height:1.45;color:var(--ink)}
  .owner-note strong{color:var(--navy);font-weight:600}

  .section-title{position:absolute;font-family:"Passion One",Impact,sans-serif;font-weight:700;font-size:54px;text-transform:uppercase;letter-spacing:.5px}
  .section-title .accent{color:var(--green-deep)}
  .commercial-title{left:60px;top:660px;color:var(--navy)}

  .checklist{position:absolute;list-style:none;display:grid;grid-template-columns:1fr 1fr;column-gap:20px;row-gap:26px;font-size:24px;font-weight:500;color:var(--ink)}
  .checklist li{display:flex;align-items:center;gap:14px;line-height:1.2}
  .checklist svg{flex:0 0 34px;width:34px;height:34px}
  .commercial-list{left:60px;top:750px;width:600px;grid-auto-flow:column;grid-template-rows:repeat(4,auto)}

  .team-illustration{position:absolute;left:690px;top:680px;width:370px;height:310px;border-radius:10px;background:linear-gradient(180deg,#eaf3fb 0%,#bcd8f0 100%)}

  .residential-band{position:absolute;left:0;top:1040px;width:1100px;height:86px}
  .residential-band .band-text{position:absolute;right:60px;top:0;height:86px;display:flex;align-items:center;font-family:"Passion One",Impact,sans-serif;font-weight:700;font-size:52px;color:#fff;text-transform:uppercase}

  .couple-illustration{position:absolute;left:50px;top:1150px;width:380px;height:360px;border-radius:10px;background:linear-gradient(180deg,#f3e6c9 0%,#8fb6df 60%,#e5a23a 100%);opacity:.8}
  .residential-list{left:470px;top:1170px;width:600px;grid-auto-flow:column;grid-template-rows:repeat(4,auto);row-gap:30px;font-size:23px}

  .footer{position:absolute;left:0;top:1560px;width:1100px;height:160px}
  .footer-phone{position:absolute;left:60px;top:1590px;display:flex;align-items:center;gap:18px;font-size:44px;font-weight:700;color:#fff}
  .footer-phone svg{width:44px;height:44px}
  .footer-web{position:absolute;right:50px;top:1675px;font-size:20px;font-weight:600;color:#fff}
</style>
</head>
<body>
<main class="flyer">
  <svg class="corner-accent" viewBox="0 0 300 110" aria-hidden="true">
    <path d="M0 0 H300 C200 20 100 50 0 90 Z" fill="var(--navy)"/>
    <path d="M0 90 C100 50 200 20 300 0 L300 12 C200 32 100 62 0 104 Z" fill="var(--green)"/>
  </svg>

  <div class="hero-photo" role="img" aria-label="Photo of a technician in a white protective suit spraying disinfectant in a bright room"></div>

  <svg class="hero-swoosh" viewBox="0 0 1100 240" preserveAspectRatio="none" aria-hidden="true">
    <path d="M480 180 C650 120 850 200 1100 150 L1100 240 L480 240 Z" fill="#ffffff"/>
    <path d="M470 190 C650 110 850 170 1100 120 L1100 140 C850 190 650 135 480 205 Z" fill="var(--blue)"/>
    <path d="M480 205 C650 140 850 200 1100 148 L1100 158 C850 210 650 155 490 215 Z" fill="var(--green)"/>
  </svg>

  <h1 class="brand-title">
    <span class="line-name">Bellhaven</span>
    <span class="line-cleaning">Cleaning &amp;</span>
    <span class="line-disinfect">Disinfecting</span>
  </h1>

  <svg class="badge" viewBox="0 0 240 240" role="img" aria-label="25 years experience seal">
    <circle cx="120" cy="120" r="116" fill="#fff" stroke="var(--navy)" stroke-width="6"/>
    <circle cx="120" cy="120" r="98" fill="none" stroke="var(--navy)" stroke-width="2"/>
    <rect x="10" y="92" width="220" height="60" fill="var(--navy)"/>
    <text x="120" y="136" text-anchor="middle" font-family="Passion One, sans-serif" font-size="46" font-weight="700" fill="#fff">25 years</text>
    <text x="120" y="72" text-anchor="middle" font-family="Poppins, sans-serif" font-size="17" font-weight="600" fill="var(--navy)" letter-spacing="3">EXCELLENCE</text>
    <text x="120" y="186" text-anchor="middle" font-family="Poppins, sans-serif" font-size="17" font-weight="600" fill="var(--navy)" letter-spacing="3">EXPERIENCE</text>
  </svg>

  <div class="mascot" role="img" aria-label="Cartoon cleaner mascot holding a spray bottle"></div>

  <p class="owner-note">Owned and operated by a licensed <strong>BSN Registered Nurse</strong> specially trained in Infection Control Prevention with over 25 years experience.</p>

  <h2 class="section-title commercial-title">Commercial <span class="accent">Cleaning</span></h2>
  <ul class="checklist commercial-list">
    <li><svg viewBox="0 0 34 34" aria-hidden="true"><circle cx="17" cy="17" r="16" fill="var(--green)"/><path d="M9 17.5l5.5 5.5L25 12" fill="none" stroke="#fff" stroke-width="3.5" stroke-linecap="round" stroke-linejoin="round"/></svg>Janitorial</li>
    <li><svg viewBox="0 0 34 34" aria-hidden="true"><circle cx="17" cy="17" r="16" fill="var(--green)"/><path d="M9 17.5l5.5 5.5L25 12" fill="none" stroke="#fff" stroke-width="3.5" stroke-linecap="round" stroke-linejoin="round"/></svg>Offices</li>
    <li><svg viewBox="0 0 34 34" aria-hidden="true"><circle cx="17" cy="17" r="16" fill="var(--green)"/><path d="M9 17.5l5.5 5.5L25 12" fill="none" stroke="#fff" stroke-width="3.5" stroke-linecap="round" stroke-linejoin="round"/></svg>Floor maintenance</li>
    <li><svg viewBox="0 0 34 34" aria-hidden="true"><circle cx="17" cy="17" r="16" fill="var(--green)"/><path d="M9 17.5l5.5 5.5L25 12" fill="none" stroke="#fff" stroke-width="3.5" stroke-linecap="round" stroke-linejoin="round"/></svg>Carpet cleaning</li>
    <li><svg viewBox="0 0 34 34" aria-hidden="true"><circle cx="17" cy="17" r="16" fill="var(--green)"/><path d="M9 17.5l5.5 5.5L25 12" fill="none" stroke="#fff" stroke-width="3.5" stroke-linecap="round" stroke-linejoin="round"/></svg>Move-ins</li>
    <li><svg viewBox="0 0 34 34" aria-hidden="true"><circle cx="17" cy="17" r="16" fill="var(--green)"/><path d="M9 17.5l5.5 5.5L25 12" fill="none" stroke="#fff" stroke-width="3.5" stroke-linecap="round" stroke-linejoin="round"/></svg>Move-outs</li>
    <li><svg viewBox="0 0 34 34" aria-hidden="true"><circle cx="17" cy="17" r="16" fill="var(--green)"/><path d="M9 17.5l5.5 5.5L25 12" fill="none" stroke="#fff" stroke-width="3.5" stroke-linecap="round" stroke-linejoin="round"/></svg>Constructions clean-ups</li>
    <li><svg viewBox="0 0 34 34" aria-hidden="true"><circle cx="17" cy="17" r="16" fill="var(--green)"/><path d="M9 17.5l5.5 5.5L25 12" fill="none" stroke="#fff" stroke-width="3.5" stroke-linecap="round" stroke-linejoin="round"/></svg>Estate clean-outs</li>
  </ul>

  <div class="team-illustration" role="img" aria-label="Illustration of a cleaning team with mops, buckets and a cart in front of an office building"></div>

  <div class="residential-band">
    <svg viewBox="0 0 1100 86" width="1100" height="86" preserveAspectRatio="none" aria-hidden="true">
      <rect width="1100" height="86" fill="var(--navy)"/>
      <path d="M0 0 H320 L280 86 H0 Z" fill="var(--navy-deep)"/>
      <path d="M300 0 H330 L290 86 H260 Z" fill="var(--green)"/>
    </svg>
    <div class="band-text">Residential Cleaning</div>
  </div>

  <div class="couple-illustration" role="img" aria-label="Illustration of two cleaners with a broom, mop and bucket"></div>

  <ul class="checklist residential-list">
    <li><svg viewBox="0 0 34 34" aria-hidden="true"><circle cx="17" cy="17" r="16" fill="var(--green)"/><path d="M9 17.5l5.5 5.5L25 12" fill="none" stroke="#fff" stroke-width="3.5" stroke-linecap="round" stroke-linejoin="round"/></svg>House cleaning</li>
    <li><svg viewBox="0 0 34 34" aria-hidden="true"><circle cx="17" cy="17" r="16" fill="var(--green)"/><path d="M9 17.5l5.5 5.5L25 12" fill="none" stroke="#fff" stroke-width="3.5" stroke-linecap="round" stroke-linejoin="round"/></svg>Before and after party</li>
    <li><svg viewBox="0 0 34 34" aria-hidden="true"><circle cx="17" cy="17" r="16" fill="var(--green)"/><path d="M9 17.5l5.5 5.5L25 12" fill="none" stroke="#fff" stroke-width="3.5" stroke-linecap="round" stroke-linejoin="round"/></svg>Move-ins</li>
    <li><svg viewBox="0 0 34 34" aria-hidden="true"><circle cx="17" cy="17" r="16" fill="var(--green)"/><path d="M9 17.5l5.5 5.5L25 12" fill="none" stroke="#fff" stroke-width="3.5" stroke-linecap="round" stroke-linejoin="round"/></svg>Move-outs</li>
    <li><svg viewBox="0 0 34 34" aria-hidden="true"><circle cx="17" cy="17" r="16" fill="var(--green)"/><path d="M9 17.5l5.5 5.5L25 12" fill="none" stroke="#fff" stroke-width="3.5" stroke-linecap="round" stroke-linejoin="round"/></svg>Holiday cleaning</li>
    <li><svg viewBox="0 0 34 34" aria-hidden="true"><circle cx="17" cy="17" r="16" fill="var(--green)"/><path d="M9 17.5l5.5 5.5L25 12" fill="none" stroke="#fff" stroke-width="3.5" stroke-linecap="round" stroke-linejoin="round"/></svg>Seasonal cleaning</li>
    <li><svg viewBox="0 0 34 34" aria-hidden="true"><circle cx="17" cy="17" r="16" fill="var(--green)"/><path d="M9 17.5l5.5 5.5L25 12" fill="none" stroke="#fff" stroke-width="3.5" stroke-linecap="round" stroke-linejoin="round"/></svg>Carpet cleaning</li>
    <li><svg viewBox="0 0 34 34" aria-hidden="true"><circle cx="17" cy="17" r="16" fill="var(--green)"/><path d="M9 17.5l5.5 5.5L25 12" fill="none" stroke="#fff" stroke-width="3.5" stroke-linecap="round" stroke-linejoin="round"/></svg>Deodorizing and sanitizing</li>
  </ul>

  <svg class="footer" viewBox="0 0 1100 160" preserveAspectRatio="none" aria-hidden="true">
    <path d="M0 20 C300 0 700 10 1100 0 V160 H0 Z" fill="var(--navy)"/>
    <path d="M520 110 H1100 V160 H480 Z" fill="var(--green)"/>
  </svg>
  <div class="footer-phone">
    <svg viewBox="0 0 24 24" aria-hidden="true"><path d="M6.6 10.8a15.1 15.1 0 006.6 6.6l2.2-2.2a1 1 0 011-.25 11.4 11.4 0 003.6.57 1 1 0 011 1V20a1 1 0 01-1 1A17 17 0 013 4a1 1 0 011-1h3.5a1 1 0 011 1c0 1.250.2 2.450.57 3.57a1 1 0 01-.25 1z" fill="#fff"/></svg>
    555-014-2890
  </div>
  <div class="footer-web">www.BellhavenCleaning.com</div>
</main>
</body>
</html>
```